Modern Yoga Studio Timetable and Flyer Design

We have a comprehensive class timetable and we are wanting to a clean modern look for our Spring timetable.

We require a double sided flyer with our class timetable included.
We would prefer an A5 size (postcard) or DL (1/3 A4).

We would like the final flyer to have.
Side A : Yoga image, logo

Fennel Stretch Hall
address: 4/71 Wexcombe Lane, Pelharton
website: fennelstretch.com.au
mobile: 0471 296 814

Side B: Clear easy to read timetable with a break down of class types and website.

We would also like to have a copy of the timetable itself as a separate jpg or pdf for use on our website to download.

Thank you.
Yours kindly,
Nell

I have attached a sample of another timetable of which I like the look and feel of, however this is just a guide. I've also attached our 'new' schedule in WORD plus uploaded our last design of the front.
Updates

Target Market(s)

Women aged 30-45

Industry/Entity Type

Health And Wellness

Font styles to use
Other font styles liked:
• Brandon Grotesque, Jenna Sue

Colors
6c459b
33a6d7
ffffff

Requirements
Must have
• A definitive colour to decipher between different class types on our timetable. Where each colour represents a different class type. Colours and layouts similar to our website design, see www.fennelstretch.com.au
Nice to have
• I've included a design of another studio whose timetable design I like. One of our own yoga images instead of a stock image.
Should not have
• No dark gridlines between the cells/boxes in the timetables. Please don't use stock yoga images.

```html
<!DOCTYPE html>
<html lang="en">
<head>
<meta charset="utf-8">
<title>Fennel Stretch Hall – Spring Timetable Flyer</title>
<link href="https://fonts.googleapis.com/css2?family=Open+Sans:wght@300;400;600;700;800&family=Oswald:wght@600&display=swap" rel="stylesheet">
<style>
  :root{
    --blue:#3f86c8;
    --blue-deep:#3a7fc1;
    --purple:#3e2a66;
    --purple-mid:#6c459b;
    --aqua:#a8dde4;
    --aqua-line:#6fb3d6;
    --day-cell:#f2f2f4;
    --time-cell:#d3dfe2;
    --ink:#1d1d1f;
    --white:#ffffff;
    --page:#e9e7e4;
  }
  *{box-sizing:border-box;margin:0;padding:0}
  html,body{width:1200px;height:1178px;overflow:hidden;background:var(--page)}
  body{position:relative;font-family:"Open Sans",sans-serif;color:var(--ink)}

  .flyer{position:absolute;top:94px;overflow:hidden;box-shadow:0 4px 14px rgba(0,0,0,.18)}
  .flyer--timetable{left:120px;width:456px;height:974px;background:var(--blue)}
  .flyer--front{left:618px;width:457px;height:970px;background:var(--white)}

  /* timetable side */
  .timetable__title{position:absolute;top:30px;left:0;width:100%;text-align:center;
    color:var(--white);font-weight:700;font-size:31px;line-height:41px;letter-spacing:.3px}
  .schedule{position:absolute;top:129px;left:18px;width:416px}
  .day-group{display:flex;margin-bottom:8px}
  .day-group__name{width:100px;background:var(--day-cell);display:flex;align-items:center;
    padding-left:8px;font-size:17px;font-weight:600}
  .day-group__slots{margin-left:9px;flex:1}
  .slot{display:flex;height:21.3px}
  .slot__time{width:108px;background:var(--time-cell);font-size:12.5px;padding-left:12px;
    display:flex;align-items:center;border-bottom:1px solid var(--white)}
  .slot__class{flex:1;margin-left:6px;background:var(--aqua);font-size:12.5px;padding-left:7px;
    display:flex;align-items:center;border-bottom:1px solid var(--aqua-line);text-transform:uppercase}
  .slot:last-child .slot__time,.slot:last-child .slot__class{border-bottom:none}
  .day-group--single .slot{height:31px}
  .day-group--single .day-group__name{height:31px}

  .timetable__band{position:absolute;top:758px;left:0;width:100%;height:18px;background:var(--purple)}
  .timetable__foot{position:absolute;top:776px;left:0;width:100%;height:178px;background:var(--white)}
  .ornament{position:absolute;border-radius:0 0 50% 50%;
    background:radial-gradient(ellipse at 50% 0%,rgba(108,69,155,.55) 0%,rgba(108,69,155,.18) 45%,rgba(200,200,215,.18) 70%,rgba(255,255,255,0) 100%)}
  .timetable__foot .ornament{left:38px;top:0;width:380px;height:150px}
  .brand-name{position:absolute;font-family:"Open Sans",sans-serif;font-weight:300;
    color:#3b86cf;letter-spacing:6px;white-space:nowrap;text-align:center}
  .timetable__foot .brand-name{left:0;width:100%;top:100px;font-size:27px}

  /* front side */
  .front__topband{position:absolute;top:0;left:0;width:100%;height:25px;background:var(--blue)}
  .flyer--front .ornament--top{left:30px;top:25px;width:400px;height:170px}
  .flyer--front .brand-name--top{left:0;width:100%;top:150px;font-size:28px}
  .front__photo{position:absolute;left:0;top:225px;width:100%;height:470px;
    background:linear-gradient(180deg,#ffffff 0%,#f4f2f1 30%,#e7dcd3 62%,#b59a7a 78%,#a88a68 100%)}
  .front__wave{position:absolute;left:0;top:0;width:457px;height:970px}
  .front__tagline{position:absolute;right:31px;top:548px;text-align:right;color:var(--white);
    font-weight:700;font-size:16px;line-height:24.5px;text-transform:uppercase;
    text-shadow:0 1px 2px rgba(0,0,0,.35)}
  .book-badge{position:absolute;left:64px;top:555px;width:157px;height:157px;border-radius:50%;
    background:var(--blue-deep);padding:5px}
  .book-badge__inner{width:100%;height:100%;border-radius:50%;
    background:radial-gradient(circle at 45% 35%,#ffffff 0%,#e6e6e8 45%,#a9aaae 100%);
    border:3px solid #f4f4f4;display:flex;align-items:center;justify-content:center;text-align:center;
    font-family:"Oswald",sans-serif;font-weight:600;font-size:27px;line-height:32px;color:#2a2a2c}
  .ornament--low{left:150px;top:660px;width:210px;height:100px;
    background:radial-gradient(ellipse at 50% 20%,rgba(62,42,102,.55) 0%,rgba(62,42,102,.2) 50%,rgba(62,42,102,0) 100%)}
  .flyer--front .brand-name--low{left:0;width:100%;top:722px;font-size:22px;color:rgba(40,90,170,.55)}
  .front__studio{position:absolute;left:0;width:100%;text-align:center;color:var(--white)}
  .front__studio-name{top:778px;font-weight:700;font-size:29px}
  .front__address{top:826px;font-weight:700;font-size:17px;letter-spacing:.3px}
  .front__mobile{top:856px;font-size:17px}
  .front__email{top:881px;font-size:16px}
  .front__mobile b,.front__email b{font-weight:700}
  .front__urlband{position:absolute;left:0;bottom:0;width:100%;height:56px;background:var(--purple);
    color:var(--white);font-weight:700;font-size:23px;display:flex;align-items:center;justify-content:center;letter-spacing:.4px}
</style>
</head>
<body>

<section class="flyer flyer--timetable" aria-label="Spring timetable side">
  <h1 class="timetable__title">FENNEL STRETCH SPRING<br>TIMETABLE</h1>

  <div class="schedule">
    <div class="day-group">
      <div class="day-group__name">Monday</div>
      <div class="day-group__slots">
        <div class="slot"><span class="slot__time">09.30 am</span><span class="slot__class">Slow Flow</span></div>
        <div class="slot"><span class="slot__time">06.00 pm</span><span class="slot__class">Pregnancy*</span></div>
        <div class="slot"><span class="slot__time">07.30 pm</span><span class="slot__class">Vinyasa Flow</span></div>
      </div>
    </div>
    <div class="day-group">
      <div class="day-group__name">Tuesday</div>
      <div class="day-group__slots">
        <div class="slot"><span class="slot__time">05.45 am</span><span class="slot__class">Rise + Shine*</span></div>
        <div class="slot"><span class="slot__time">09.15 am</span><span class="slot__class">Vinyasa Flow</span></div>
        <div class="slot"><span class="slot__time">11.00 pm</span><span class="slot__class">Mum + Baby*</span></div>
        <div class="slot"><span class="slot__time">06.00 pm</span><span class="slot__class">Vinyasa Flow</span></div>
        <div class="slot"><span class="slot__time">07.30 pm</span><span class="slot__class">Pregnancy*</span></div>
      </div>
    </div>
    <div class="day-group">
      <div class="day-group__name">Wednesday</div>
      <div class="day-group__slots">
        <div class="slot"><span class="slot__time">04.00 pm</span><span class="slot__class">Kids 8-12*</span></div>
        <div class="slot"><span class="slot__time">04.45 pm</span><span class="slot__class">Teens</span></div>
        <div class="slot"><span class="slot__time">06.00 pm</span><span class="slot__class">Slow Flow</span></div>
        <div class="slot"><span class="slot__time">07.30 pm</span><span class="slot__class">Yin + Restore</span></div>
      </div>
    </div>
    <div class="day-group">
      <div class="day-group__name">Thursday</div>
      <div class="day-group__slots">
        <div class="slot"><span class="slot__time">05.45 am</span><span class="slot__class">Rise + Shine*</span></div>
        <div class="slot"><span class="slot__time">09.30 am</span><span class="slot__class">Vinyasa Flow</span></div>
        <div class="slot"><span class="slot__time">11.00 am</span><span class="slot__class">Mum + Baby*</span></div>
        <div class="slot"><span class="slot__time">12.15 pm</span><span class="slot__class">Pregnancy</span></div>
        <div class="slot"><span class="slot__time">04.00 pm</span><span class="slot__class">Kids&nbsp; 5- 7*</span></div>
        <div class="slot"><span class="slot__time">05.00 pm</span><span class="slot__class">500PM</span></div>
        <div class="slot"><span class="slot__time">06.15 pm</span><span class="slot__class">Pregnancy*</span></div>
        <div class="slot"><span class="slot__time">07.30 pm</span><span class="slot__class">Women’s Wellness*</span></div>
      </div>
    </div>
    <div class="day-group day-group--single">
      <div class="day-group__name">Friday</div>
      <div class="day-group__slots">
        <div class="slot"><span class="slot__time">06.00 pm</span><span class="slot__class">Flow + Restore</span></div>
      </div>
    </div>
    <div class="day-group">
      <div class="day-group__name">Saturday</div>
      <div class="day-group__slots">
        <div class="slot"><span class="slot__time">09.00 am</span><span class="slot__class">Vinyasa Flow</span></div>
        <div class="slot"><span class="slot__time">10.30 pm</span><span class="slot__class">Pregnancy*</span></div>
        <div class="slot"><span class="slot__time">04.00 pm</span><span class="slot__class">Vinyasa Flow</span></div>
      </div>
    </div>
    <div class="day-group day-group--single">
      <div class="day-group__name">Sunday</div>
      <div class="day-group__slots">
        <div class="slot"><span class="slot__time">09.15 pm</span><span class="slot__class">Yin</span></div>
      </div>
    </div>
  </div>

  <div class="timetable__band"></div>
  <div class="timetable__foot">
    <div class="ornament" role="img" aria-label="Faint purple mandala ornament"></div>
    <div class="brand-name">fennel stretch hall</div>
  </div>
</section>

<section class="flyer flyer--front" aria-label="Studio front side">
  <div class="front__topband"></div>
  <div class="ornament ornament--top" role="img" aria-label="Purple mandala ornament"></div>
  <div class="brand-name brand-name--top">fennel stretch hall</div>

  <div class="front__photo" role="img" aria-label="Photo of a yoga teacher in a twisted side-angle pose on a woven mat"></div>

  <svg class="front__wave" viewBox="0 0 457 970" aria-hidden="true">
    <path d="M0,700 C110,600 200,662 300,655 C370,650 420,640 457,622 L457,970 L0,970 Z" fill="#3f86c8"/>
    <path d="M0,700 C110,600 200,662 300,655 C370,650 420,640 457,622" fill="none" stroke="#d4d5d8" stroke-width="6"/>
  </svg>

  <p class="front__tagline">Inclusive, inspiring<br>Bouitique&nbsp; yoga studio<br>classes for all ages<br>+ abilities</p>

  <div class="ornament ornament--low" role="img" aria-label="Faint mandala ornament"></div>
  <div class="brand-name brand-name--low">fennel stretch hall</div>

  <div class="book-badge"><div class="book-badge__inner">BOOK<br>ONLINE<br>NOW</div></div>

  <h2 class="front__studio front__studio-name">Fennel Stretch Hall</h2>
  <p class="front__studio front__address">4/71 Wexcombe Lane, Pelharton</p>
  <p class="front__studio front__mobile">Mobile: <b>0471 296 814</b></p>
  <p class="front__studio front__email">email: <b>hello@fennelstretch.com.au</b></p>

  <div class="front__urlband">www.fennelstretch.com.au</div>
</section>

</body>
</html>
```